Kleine Website f. Unternehmensdarstellung
Zielgruppe
Geschäftsführer, Marketing & Sales Manager asiatischer Konzerne.
Aufgabenstellung
Wir sind eine Consulting und Handelsagentur mit überwiegend internationaler Kundschaft (Asien 70%).
Für einen Webauftritt, ca. 8 Seiten, haben wir eine Powerpoint Vorlage erstellt, diese zeigt nur die Inhalte. Wir benötigen nun daraus eine Website, haben eigenen Webspace, eigener Server bei Hostquelle. Wir stellen uns als Hintergrundbild auf der Frontpage Hongkong vor. Keine Flash videos oder audio einbindung ! Sprache Englisch, die Texte sollten von uns leicht editierbar sein, falls mal Anpassungen gemacht werden müssen.

```html
<!DOCTYPE html>
<html lang="en">
<head>
<meta charset="utf-8">
<title>Veltaro Group – Technology Finance</title>
<link rel="stylesheet" href="https://fonts.googleapis.com/css2?family=Noto+Sans:wght@400;700&display=swap">
<style>
  :root {
    --page-bg: #0c0c0d;
    --sky-top: #0b0b0c;
    --sky-mid: #1d1d22;
    --city-glow: #5a4c38;
    --city-light: #8c7a5a;
    --water: #2a2622;
    --header-text: #f2f2f2;
    --panel-bg: rgba(228, 228, 230, 0.84);
    --body-text: #1b1b1b;
    --footer-link: #8a8a8a;
    --footer-copy: #6e6e6e;
  }
  * { margin: 0; padding: 0; box-sizing: border-box; }
  html, body {
    width: 1200px; height: 696px; overflow: hidden;
    background: var(--page-bg);
    font-family: "Noto Sans", sans-serif;
  }
  .site {
    position: relative; width: 1200px; height: 696px; overflow: hidden;
  }
  .skyline {
    position: absolute; inset: 0;
    background:
      radial-gradient(ellipse 260px 420px at 920px 300px, rgba(220,220,230,0.28), transparent 70%),
      radial-gradient(ellipse 300px 160px at 160px 420px, rgba(230,220,200,0.25), transparent 70%),
      linear-gradient(180deg,
        var(--sky-top) 0%,
        var(--sky-mid) 35%,
        var(--city-glow) 62%,
        var(--city-light) 78%,
        var(--water) 88%,
        var(--page-bg) 94%);
  }
  .site-header .welcome {
    position: absolute; left: 198px; top: 18px;
    font-size: 19px; color: var(--header-text); font-weight: 400;
  }
  .brand {
    position: absolute; right: 199px; top: 14px;
    display: flex; align-items: center; gap: 10px;
  }
  .brand-mark {
    width: 22px; height: 22px; background: var(--header-text);
  }
  .brand-name {
    font-size: 30px; font-weight: 700; color: var(--header-text);
    letter-spacing: 4px; line-height: 1;
  }
  .intro {
    position: absolute; left: 0; width: 1200px; top: 76px;
    text-align: center; font-size: 18px; color: var(--header-text);
    padding-left: 40px;
  }
  .content-panel {
    position: absolute; left: 198px; top: 120px;
    width: 804px; height: 502px;
    background: var(--panel-bg); border-radius: 4px;
  }
  .content-panel h1 {
    position: absolute; left: 32px; top: 28px;
    font-size: 20px; font-weight: 700; color: #000;
  }
  .content-panel p {
    position: absolute; left: 31px; width: 740px;
    font-size: 14px; line-height: 20px; color: var(--body-text);
  }
  .content-panel .indent { left: 33px; }
  .content-panel .loose { line-height: 27px; }
  .site-footer nav {
    position: absolute; top: 640px; left: 0; width: 1200px;
    display: flex; justify-content: center; gap: 0;
    font-size: 10px; padding-right: 5px;
  }
  .site-footer a {
    color: var(--footer-link); text-decoration: none; margin: 0 15px;
  }
  .site-footer .copyright {
    position: absolute; top: 661px; left: 0; width: 1200px;
    text-align: center; font-size: 10px; color: var(--footer-copy);
  }
</style>
</head>
<body>
<div class="site">
  <div class="skyline" role="img" aria-label="Night view of the Hong Kong skyline with lit towers and harbour"></div>

  <header class="site-header">
    <div class="welcome">Welcome to the Veltaro Group...</div>
    <div class="brand">
      <span class="brand-mark"></span>
      <span class="brand-name">VELTARO</span>
    </div>
  </header>

  <div class="intro">Our business segments cover quite an area, please select your piont of interest :</div>

  <main class="content-panel">
    <h1>Technology Finance</h1>
    <p class="indent" style="top:64px">Quite often the best idea or product does loose significant profits, because the market entrance is slowed by lacking funds and enthusiastic entepreneurs</p>
    <p style="top:118px">Quite often you are squeezed out of a good idea, because your bank just plays a bad game</p>
    <p class="loose" style="top:153px">Quite often your investors lack technological experience...thus they just do not understand, what you try to explain. Even Anton Ferrel stalled on this...</p>
    <p style="top:226px">Quite often students or graduates have huge ideas, but are alone in the dark with nobody to listen...<br>and to finance.</p>
    <p style="top:285px">Here is our promise:</p>
    <p style="top:322px">We have been through all of this on our own – thus we know, what you are talking about.</p>
    <p style="top:359px">If you enter a candid description of what is going on, we will:<br>Read &amp; think &amp; come back to you in a timely manner with a solid and reliable answer</p>
  </main>

  <footer class="site-footer">
    <nav>
      <a href="#">Home</a>
      <a href="#">Agency</a>
      <a href="#">Consultancy</a>
      <a href="#">Technology Finance</a>
      <a href="#">Troubleshooting</a>
      <a href="#">M&amp;A Silent Service</a>
    </nav>
    <div class="copyright">Copyright 2010. Veltaro Group. All Rights Reserved.</div>
  </footer>
</div>
</body>
</html>
```